Invitation/Flyer Design Project

Scope of Project: Faxable/printable/emailable/downloadable flyer/invitation to our User Group Meeting including a registration form. This User Group Meeting is tool we use to better communicate with our customers as to the changes in the software and to hear and learn from other customers and their use of the software. It is a 3 day event where our customers come to us to learn and share. We will NOT be professionally printing this flyer/invite.

Design:
• Design in a Microsoft or Adobe tool. We will also need a pdf file for download from landing page.
• Colors must be easy to print (especially in registration form area) as this flyer will NOT be a mailer with professional printing
• You have creative license with design and layout
• VRT logo attached.
• Text and contect attached (some voids have been noted as we work out details)

About VRT: VRT is a software and consulting services company specializing in quality management in a manufacturing environment including automotive, medical device and aerospace & defense. We have been in business since 1988 which is the longest in the industry.

Possible themes – use artwork as needed with the focus on moving forward (this will be an area for more of your creativity)
• Amplify
• Trail Blazing
• Accelerating

Target Market(s)

quality managment professionals in manufacturing

Industry/Entity Type

Environment

Requirements
Must have
• Graphics and feel that we are moving forward! We are a software company so a technology focus is a bonus.
Nice to have
• Here are some clues as to the colors we usually use (but not necessarily needed).

VRT colors are (in case you need them):
Dark Blue: (PMS 5405)
R: 60 G: 113 B:144

Gold: (PMS 125)
R: 197 G: 150 B:11

Light Blue: (PMS 644)
R: 137 G: 171 B:191

Tan: (PMS 7530)
R: 217 G: 209 B:196

Burnt Orange: (PMS 471)
R: 182 G: 85 B:24

```html
<!DOCTYPE html>
<html lang="en">
<head>
<meta charset="utf-8">
<title>VRT User Group Meeting – Invitation</title>
<link rel="stylesheet" href="https://fonts.googleapis.com/css2?family=Squada+One&family=Bowlby+One&family=Arimo:wght@400&display=swap">
<style>
  :root {
    --stage: #000000;
    --paper: #ffffff;
    --paper-mist: #f7f9fa;
    --brand-blue: #3c7190;
    --brand-teal: #6fb6c3;
    --brand-gold: #c5960b;
    --ink-dark: #151c22;
    --ink-body: #2b2f33;
    --wash-light: #dff3f7;
    --wash-mid: #8fd0dc;
    --wash-deep: #1f5f6c;
    --folio: #555555;
  }
  * { margin: 0; padding: 0; box-sizing: border-box; }
  html, body { width: 1200px; height: 900px; overflow: hidden; background: var(--stage); }
  .canvas { position: relative; width: 1200px; height: 900px; background: var(--stage); }

  .page { position: absolute; top: 75px; width: 517px; height: 730px; background: var(--paper); overflow: hidden; }
  .page--cover { left: 75px; }
  .page--inside { left: 614px; }

  /* cover */
  .cover__mist { position: absolute; left: 0; top: 143px; width: 100%; height: 190px; background: var(--paper-mist); }
  .cover__artwork {
    position: absolute; left: 0; top: 330px; width: 100%; height: 322px;
    background:
      radial-gradient(ellipse 60% 22% at 55% 38%, rgba(31,95,108,.75), rgba(31,95,108,0) 70%),
      radial-gradient(ellipse 75% 45% at 50% 45%, var(--wash-mid), rgba(143,208,220,0) 75%),
      linear-gradient(180deg, var(--paper-mist) 0%, var(--wash-light) 40%, var(--paper) 100%);
  }
  .cover__brand { position: absolute; left: 0; top: 170px; width: 100%; display: flex; align-items: center; justify-content: center; gap: 16px; }
  .brand-dot { width: 22px; height: 22px; border-radius: 50%; background: var(--brand-gold); }
  .brand-name { font-family: "Squada One", sans-serif; font-size: 150px; line-height: 1; color: var(--brand-blue); letter-spacing: 2px; }
  .cover__event {
    position: absolute; left: 0; top: 345px; width: 100%; text-align: center;
    font-family: "Squada One", sans-serif; font-size: 34px; line-height: 1; color: var(--brand-gold); letter-spacing: 1px;
  }
  .cover__when {
    position: absolute; left: 0; top: 536px; width: 100%; text-align: center;
    font-family: "Bowlby One", sans-serif; font-size: 14.5px; line-height: 16px; color: var(--ink-dark);
  }
  .cover__band { position: absolute; left: 0; top: 652px; width: 100%; height: 35px; background: linear-gradient(90deg, var(--brand-blue) 0%, var(--brand-blue) 35%, var(--brand-teal) 75%, var(--brand-teal) 100%); }

  /* inside */
  .inside__artwork {
    position: absolute; left: 0; top: 0; width: 330px; height: 100%;
    background:
      radial-gradient(ellipse 30% 55% at 18% 40%, rgba(31,95,108,.8), rgba(31,95,108,0) 70%),
      radial-gradient(ellipse 55% 70% at 25% 45%, var(--wash-mid), rgba(143,208,220,0) 80%),
      linear-gradient(90deg, var(--wash-mid) 0%, var(--wash-light) 60%, rgba(255,255,255,0) 100%);
  }
  .inside__band { position: absolute; left: 448px; top: 0; width: 52px; height: 100%; background: linear-gradient(180deg, var(--brand-teal) 0%, var(--brand-teal) 40%, var(--brand-blue) 70%, var(--brand-blue) 100%); }
  .inside__content { position: absolute; left: 226px; top: 115px; width: 192px; }
  .section { margin-bottom: 0; }
  .section__title { font-family: "Squada One", sans-serif; font-size: 15.5px; line-height: 14px; color: var(--brand-gold); text-transform: uppercase; }
  .section__list { list-style: none; font-family: "Arimo", sans-serif; font-size: 11.6px; line-height: 14.6px; color: var(--ink-body); }
  .section__list li::before { content: "•"; }
  .section--experience { position: absolute; top: 0; }
  .section--audience { position: absolute; top: 115px; }
  .section--reasons { position: absolute; top: 229px; }
  .section__text { margin-top: 4px; font-family: "Arimo", sans-serif; font-size: 11.6px; line-height: 14.6px; color: var(--ink-body); text-align: justify; hyphens: manual; }
  .inside__brand { position: absolute; left: 376px; top: 695px; font-family: "Squada One", sans-serif; font-size: 34px; line-height: 1; color: var(--brand-blue); }

  .folio { position: absolute; top: 811px; font-family: "Squada One", sans-serif; font-size: 28px; line-height: 1; color: var(--folio); }
  .folio--one { left: 569px; }
  .folio--two { left: 1106px; }
</style>
</head>
<body>
<main class="canvas">
  <section class="page page--cover">
    <div class="cover__mist"></div>
    <div class="cover__artwork" role="img" aria-label="Abstract teal motion blur suggesting speed and moving forward"></div>
    <div class="cover__brand">
      <span class="brand-name">VRT</span>
      <span class="brand-dot"></span>
    </div>
    <div class="cover__event">USER GROUP MEETING</div>
    <p class="cover__when">19 - 21 september 2012<br>cleveland, oh</p>
    <div class="cover__band"></div>
  </section>

  <section class="page page--inside">
    <div class="inside__artwork" role="img" aria-label="Abstract teal streaks rushing toward the viewer"></div>
    <div class="inside__band"></div>
    <div class="inside__content">
      <div class="section section--experience">
        <h2 class="section__title">You will experience:</h2>
        <ul class="section__list">
          <li>Our new product roadmap strategy</li>
          <li>Hands-on system training</li>
          <li>Technology and consulting support</li>
          <li>A forum for communication</li>
        </ul>
      </div>
      <div class="section section--audience">
        <h2 class="section__title">Who should attend?</h2>
        <ul class="section__list">
          <li>All VRT System Users</li>
          <li>Quality Professionals</li>
          <li>IT Professionals</li>
          <li>Operations Professionals</li>
        </ul>
      </div>
      <div class="section section--reasons">
        <h2 class="section__title">Why you should attend:</h2>
        <p class="section__text">Gather with VRT at this year’s User Group Meeting to learn more about upcoming VRT software advance&shy;ments, have the opportunity to learn from other system users and have personal time with our technology and implementation staff. Attendees will learn how to maximize their in&shy;vestment in VRT with the training, one-on-one consultations and roundtable discussions with other users and staff. This User Group Meeting offers a tremendous value with the focus on moving forward in this fast-paced industry. Come learn about key advancements in what VRT has to offer and be a part of the future.</p>
      </div>
    </div>
    <div class="inside__brand">VRT</div>
  </section>

  <span class="folio folio--one">01</span>
  <span class="folio folio--two">02</span>
</main>
</body>
</html>
```